Feng shui business card for immigration law firm

Immigration law firm would like to create the business card based and look like the Green Card (lawful permanent resident card of USA). Attached please see the sample of American Green Card. The whole business card should be performed based on the FENG SHUI style: no sharp angles. Please delete all letters and fingerprint on the sample green card and put info the following order.

Target Market(s)

Immigration clients in USA

Industry/Entity Type

Business

Contact Information for Business Card

Immigration law firm would like to create the business card based and look like the Green Card (lawful permanent resident card of USA). Attached please see the sample of American Green Card. The whole business card should be performed based on the FENG SHUI style: no sharp angles. Please delete all letters on sample green card and put info the following order:

TOLAN BERIKSOVA, ESQ.
BERIKSOVA LAW GROUP, P.A.
PRACTICE LIMITED TO IMMIGRATION LAW

4370 WEST CORVINDALE PARK BOULVERD
SUITE #218
CORVINDALE PARK, FLORIDA 33174

PHONE: 754-555-0162
EMAIL: TBERIKSOVA@QUELMAIL.EXAMPLE
WEBSITE: WWW.ZORVEL-VISAHELP.EXAMPLE

The tips for the best business card
1. It is recommended to avoid using sharp points in the logo because such logos generate negative energy. Never use sharp and pointed element like spears, knives or swords in your logo.
2. One of the most essential elements in Feng Shui good flow and space which means that there should not be any obstruction, for example, there should not be any border around the card as it stop the energy flow.
3. Keep clear of clutter – Just like applying this feng shui concept to home and office, it should also be applied to designing your name card. Always keep your card as clean and concise as possible by removing all redundant information and put only relevant ones.
4. Name should not be placed in the center of the card because it cause stress and pressure to the owner.

Font styles to use
Other font styles liked:
• Garamond or Times New Roman

Requirements
Must have
• Feng shui business card

```html
<!DOCTYPE html>
<html lang="en">
<head>
<meta charset="utf-8">
<title>Beriksova Law Group – Business Card</title>
<link href="https://fonts.googleapis.com/css2?family=Tinos:wght@400;700&display=swap" rel="stylesheet">
<style>
  :root {
    --backdrop: #3a322d;
    --card: #141414;
    --card-edge: #1d1d1d;
    --ink: #f2f0ec;
    --ink-soft: #d9d6d0;
    --gold: #f0a020;
    --rule: #8a8782;
  }
  * { box-sizing: border-box; margin: 0; padding: 0; }
  html, body {
    width: 1200px; height: 780px; overflow: hidden;
    background: var(--backdrop);
  }
  .stage {
    width: 1200px; height: 780px;
    display: flex; align-items: center; justify-content: center; gap: 40px;
  }
  .card {
    position: relative;
    width: 540px; height: 309px;
    background: var(--card);
    border-radius: 14px;
    box-shadow: 0 10px 30px rgba(0,0,0,.45);
    font-family: "Tinos", "Times New Roman", serif;
    color: var(--ink);
  }
  .emblem {
    position: absolute;
    border-radius: 50%;
    border: 2px solid var(--gold);
    background: radial-gradient(circle at 50% 50%, #2a2118 0%, #0b0b0b 55%, #1a1308 100%);
  }
  .card-front .emblem { left: 28px; top: 40px; width: 132px; height: 132px; }
  .divider {
    position: absolute; left: 190px; top: 28px; width: 1px; height: 250px;
    background: var(--rule);
  }
  .details { position: absolute; left: 208px; top: 32px; right: 20px; }
  .firm { font-size: 21px; line-height: 1.05; }
  .practice { font-size: 12px; color: var(--ink-soft); margin-top: 1px; }
  .attorney { font-size: 18px; margin-top: 8px; line-height: 1; }
  .suffix { font-size: 12px; color: var(--ink-soft); margin-top: 2px; }
  .contacts { list-style: none; margin-top: 22px; font-size: 13.5px; line-height: 1.45; }
  .contacts li { display: flex; align-items: flex-start; gap: 8px; }
  .icon { flex: 0 0 11px; width: 11px; height: 11px; margin-top: 4px; }
  .address { display: block; }
  .card-back .emblem {
    left: 50%; top: 50%; width: 172px; height: 172px;
    transform: translate(-50%, -50%);
  }
</style>
</head>
<body>
<main class="stage">
  <section class="card card-front" aria-label="Business card front">
    <div class="emblem" role="img" aria-label="Circular emblem with two golden koi fish and a calligraphic character"></div>
    <div class="divider"></div>
    <div class="details">
      <h1 class="firm">Beriksova Law Group, P.A.</h1>
      <p class="practice">Practice Limited To Immigration Law</p>
      <p class="attorney">Tolan Beriksova</p>
      <p class="suffix">ESQ</p>
      <ul class="contacts">
        <li>
          <svg class="icon" viewBox="0 0 11 11"><rect width="11" height="11" rx="2" fill="var(--gold)"/><path d="M3.2 2.4c.5 0 1 1.3 1 1.6 0 .4-.6.5-.5.9.3.7.8 1.2 1.4 1.4.4.1.5-.5.9-.5.3 0 1.6.5 1.6 1 0 .6-.8 1.1-1.4 1.1C4.2 7.9 3 6.6 2.6 3.8c0-.6.2-1.4.6-1.4z" fill="#141414"/></svg>
          <span>754-555-0162</span>
        </li>
        <li>
          <svg class="icon" viewBox="0 0 11 11"><rect width="11" height="11" rx="2" fill="var(--gold)"/><rect x="2.2" y="3.2" width="6.6" height="4.6" rx=".6" fill="none" stroke="#141414" stroke-width="1"/><path d="M2.4 3.5l3.1 2.3 3.1-2.3" fill="none" stroke="#141414" stroke-width="1"/></svg>
          <span>tberiksova@quelmail.example</span>
        </li>
        <li>
          <svg class="icon" viewBox="0 0 11 11"><rect width="11" height="11" rx="2" fill="var(--gold)"/><circle cx="5.5" cy="5.5" r="3.1" fill="none" stroke="#141414" stroke-width="1"/><path d="M2.4 5.5h6.2M5.5 2.4c-1.4 1.7-1.4 4.5 0 6.2M5.5 2.4c1.4 1.7 1.4 4.5 0 6.2" fill="none" stroke="#141414" stroke-width=".8"/></svg>
          <span>www.zorvel-visahelp.example</span>
        </li>
        <li>
          <svg class="icon" viewBox="0 0 11 11"><rect width="11" height="11" rx="2" fill="var(--gold)"/><path d="M5.5 9.2C3.9 7.3 3.2 6 3.2 4.6a2.3 2.3 0 0 1 4.6 0c0 1.4-.7 2.7-2.3 4.6z" fill="#141414"/><circle cx="5.5" cy="4.6" r=".8" fill="var(--gold)"/></svg>
          <span class="address">4370 West Corvindale Park Boulverd<br>Suite #218 Corvindale Park, Florida 33174</span>
        </li>
      </ul>
    </div>
  </section>

  <section class="card card-back" aria-label="Business card back">
    <div class="emblem" role="img" aria-label="Circular emblem with two golden koi fish and a calligraphic character"></div>
  </section>
</main>
</body>
</html>
```